Business Card Design for Cybersecurity Company - QuorvaNet Systems

We need a business card design for our new cybersecurity company, QuorvaNet. We’re going for a clean, hi tech look that feels modern, premium, and trustworthy. We want a design that really stands out and makes people say WOW when we hand it over!

QuorvaNet delivers reliable IT support and managed services for small and mid sized businesses. We help companies stay secure, efficient, and connected through proactive monitoring, cybersecurity services, cloud management, and remote support.

Target Market(s)

Designers should target small and mid sized businesses that need dependable cybersecurity and IT support.

Industry/Entity Type

Cybersecurity, Managed Service Provider, IT services

Contact Information for Business Card

Contact information

Requirements
Must have
• The card should look clean, modern, and tech focused, with the QuorvaNet logo, clear contact info, and strong readability. It needs to feel premium and professional while still keeping a simple layout that fits a cybersecurity and IT brand.
Nice to have
• Nice to have elements include subtle touches that give the card a modern, tech feel, along with a layout that works well in different background styles.
Should not have
• The card should avoid clutter, loud graphics, or anything that takes attention away from the logo and contact details.

```html
<!DOCTYPE html>
<html lang="en">
<head>
<meta charset="utf-8">
<title>QuorvaNet Systems – Business Card</title>
<link href="https://fonts.googleapis.com/css2?family=Montserrat:wght@400;500;700&display=swap" rel="stylesheet">
<style>
  :root {
    --stage: #3a3a3a;
    --card-black: #050505;
    --card-white: #ffffff;
    --brand-blue: #4a6fbf;
    --brand-purple: #6a4aa6;
    --ink: #1c1c1c;
    --wash: #eef0f8;
  }
  * { box-sizing: border-box; margin: 0; padding: 0; }
  html, body { width: 1200px; height: 875px; overflow: hidden; }
  body {
    background: var(--stage);
    font-family: "Montserrat", sans-serif;
    position: relative;
  }
  .card {
    position: absolute;
    width: 540px;
    height: 309px;
    border-radius: 18px;
    overflow: hidden;
    top: 283px;
  }
  .card-back { left: 40px; background: var(--card-black); }
  .card-front { left: 620px; background: var(--card-white); }

  .wordmark { position: absolute; display: flex; align-items: center; gap: 14px; }
  .wordmark-square { width: 46px; height: 46px; }
  .wordmark-name { font-weight: 700; font-size: 44px; line-height: 1; letter-spacing: 0.5px; }
  .wordmark-sub { font-weight: 400; font-size: 15px; letter-spacing: 9px; margin-top: 6px; }

  .card-back .wordmark { left: 50%; top: 50%; transform: translate(-50%, -50%); }
  .card-back .wordmark-square { border: 4px solid #fff; }
  .card-back .wordmark-name, .card-back .wordmark-sub { color: #fff; }

  .circuit-wash {
    position: absolute; left: 190px; top: 30px; width: 300px; height: 220px;
    background: radial-gradient(ellipse at center, var(--wash) 0%, rgba(238,240,248,0) 70%);
  }
  .card-front .wordmark { left: 120px; top: 52px; }
  .card-front .wordmark-square { border: 4px solid var(--brand-blue); }
  .card-front .wordmark-name, .card-front .wordmark-sub { color: var(--brand-blue); }

  .holder { position: absolute; left: 40px; top: 180px; }
  .holder-name { font-weight: 700; font-size: 25px; color: var(--brand-blue); }
  .holder-role { font-weight: 500; font-size: 12.5px; color: var(--ink); margin-top: 6px; }

  .divider { position: absolute; left: 322px; top: 160px; width: 1.5px; height: 90px; background: var(--brand-blue); }

  .contacts { position: absolute; left: 336px; top: 160px; list-style: none; }
  .contacts li { display: flex; align-items: center; gap: 8px; font-size: 12.5px; font-weight: 500; color: var(--ink); height: 22px; }
  .contacts svg { width: 12px; height: 12px; fill: var(--brand-purple); flex: none; }

  .band { position: absolute; left: 0; bottom: 0; width: 540px; height: 309px; pointer-events: none; }
</style>
</head>
<body>
  <section class="card card-back" aria-label="Card back">
    <div class="wordmark">
      <div class="wordmark-square"></div>
      <div>
        <div class="wordmark-name">QuorvaNet</div>
        <div class="wordmark-sub">Systems</div>
      </div>
    </div>
  </section>

  <section class="card card-front" aria-label="Card front">
    <div class="circuit-wash" role="img" aria-label="Faint circuit line pattern in pale lavender"></div>
    <div class="wordmark">
      <div class="wordmark-square"></div>
      <div>
        <div class="wordmark-name">QuorvaNet</div>
        <div class="wordmark-sub">Systems</div>
      </div>
    </div>

    <div class="holder">
      <div class="holder-name">Dorian Kessler</div>
      <div class="holder-role">Owner | CEO | QuorvaNet Systems</div>
    </div>

    <div class="divider"></div>

    <ul class="contacts">
      <li><svg viewBox="0 0 12 12"><path d="M1 4 Q6 0 11 4 L9 6 L8 4.5 Q6 4 4 4.5 L3 6 Z M2 7 H10 V11 H2 Z"/></svg>(855) 340-7182</li>
      <li><svg viewBox="0 0 12 12"><path d="M2 1 L4.5 1 L5.5 4 L4 5 Q5 7.5 7 8 L8 6.5 L11 7.5 L11 10 Q6 11.5 1 3 Z"/></svg>(813) 620-3947</li>
      <li><svg viewBox="0 0 12 12"><path d="M1 2.5 H11 V9.5 H1 Z M1.5 3 L6 6.5 L10.5 3" stroke="#fff" stroke-width="0.8"/></svg>dorian@quorvanet.com</li>
      <li><svg viewBox="0 0 12 12"><circle cx="6" cy="6" r="5"/><path d="M1 6 H11 M6 1 Q3 6 6 11 M6 1 Q9 6 6 11" stroke="#fff" stroke-width="0.7" fill="none"/></svg>www.quorvanet.com</li>
    </ul>

    <svg class="band" viewBox="0 0 540 309" aria-hidden="true">
      <polygon points="0,295 400,289 380,309 0,309" fill="var(--brand-blue)"/>
      <polygon points="410,289 540,250 540,309 390,309" fill="var(--brand-purple)"/>
    </svg>
  </section>
</body>
</html>
```